Webdesign für Hunde- und Katzenernährungsberatung
Zielgruppe
Hunde und Katzenernährungsberatung, für Menschen, die auch bei ihren Hunden und Katzen auf gesunde, natürliche Ernährung achten wollen, ohne unnötigen Geschmacksverstärker, Zucker, Zusatzstoffe, etc. die gesundheitliche Probleme bei den Tieren verursachen können.
Umstellung auf natürliche, artgerechte Fütterung, teils roh, teils gekocht, angepasst auf Grösse, Rasse, Alter etc., auch speziell für Welpen
Beratung bei:
Übergewicht
Allergien
Unverträglichkeiten
Magen-Darm Problemen
individuelle Ernährungspläne
Selbsthergestellte Kekse, Leckerlies, Snacks, Pralinen und div. Hausmannskost in Einmachgläsern (alles auf Vorbestellung).
Diverse Accessoires
Halsbänder, Leinen, Geschirr aus div. natürlichen Materialien
Lern- und Spielzeug aus Holz und Stoff
div. Zubehör für Tiere, sowie auch für Frauchen und Herrchen
Aufgabenstellung
Die Seite sollte stilvoll aber nicht überfüllt sein und im Retro/Vintage Stil gehalten werden, da das Logo bereits sehr wirksam und eher auffällig ist, dezente Töne im Hintergrund, die Nahrungsmittel werden dann ev. auf Schieferplatten oder unauffälligem Hintergrund platziert. Ich sollte zu einem späteren Zeitpunkt selber Fotos, Links, Texte, etc. einfach dazu fügen können.

```html
<!DOCTYPE html>
<html lang="de">
<head>
<meta charset="utf-8">
<title>Velora – Ernährungsberatung für Hund und Katze</title>
<link rel="stylesheet" href="https://fonts.googleapis.com/css2?family=Oswald:wght@300;400;500&family=PT+Serif:ital@0;1&family=Roboto:wght@400;500&display=swap">
<style>
:root{
  --blue:#9fc4da;
  --blue-dark:#7fb0cc;
  --ink:#2b2b2b;
  --text:#777;
  --light:#f6f6f6;
  --dark:#2e2e30;
  --accent:#e8673c;
  --green:#8dc63f;
  --white:#fff;
}
*{margin:0;padding:0;box-sizing:border-box}
html,body{width:1200px;height:4532px;overflow:hidden}
body{position:relative;background:var(--white);font-family:"PT Serif",serif;color:var(--text);font-size:11px;line-height:1.45}
.abs{position:absolute}
.head{font-family:"Oswald",sans-serif;text-transform:uppercase;color:var(--ink);font-weight:400;letter-spacing:.3px}
.title{font-family:"Oswald",sans-serif;text-transform:uppercase;color:var(--blue);font-weight:400;font-size:28px;text-align:center;width:1200px;left:0;letter-spacing:.5px}
.sub{text-align:center;width:1200px;left:0;font-size:11px;color:#999}
.nav a{position:absolute;top:47px;font-family:"Roboto",sans-serif;font-size:10px;color:var(--ink);text-decoration:none;letter-spacing:.4px}
.nav a.active{color:var(--blue)}
.logo{left:551px;top:0;width:100px;height:88px;background:var(--blue);border-radius:0 0 50px 50px;display:flex;align-items:center;justify-content:center;font-family:"Oswald",sans-serif;color:var(--white);font-size:20px;font-weight:500;letter-spacing:1px;padding-bottom:12px;z-index:3}
.hero-photo{left:0;top:79px;width:1200px;height:501px;background:linear-gradient(100deg,#5a3d22 0%,#8a6437 30%,#b39a6c 55%,#7c7c52 75%,#4f5535 100%)}
.hero-shade{left:0;top:79px;width:1200px;height:501px;background:linear-gradient(90deg,rgba(0,0,0,.15),rgba(0,0,0,.3) 50%,rgba(0,0,0,0))}
.hero-name{left:246px;top:284px;font-family:"Oswald",sans-serif;font-size:40px;line-height:1;color:var(--blue);font-weight:400}
.hero-line1{left:410px;top:302px;font-family:"Oswald",sans-serif;font-size:18px;line-height:1.2;color:var(--white)}
.hero-line2{left:283px;top:328px;font-family:"Oswald",sans-serif;font-size:18px;line-height:1.2;color:var(--white)}
.hero-rule{left:283px;top:358px;width:430px;height:1px;background:rgba(255,255,255,.6)}
.hero-text{left:285px;top:375px;width:310px;color:var(--white);font-size:11px;line-height:1.3}
.hero-link{left:285px;top:436px;color:var(--white);font-family:"Oswald",sans-serif;font-size:9px;display:flex;align-items:center;gap:8px}
.dot{width:10px;height:10px;border-radius:50%;background:var(--blue);display:inline-block}
.welcome-title{left:243px;top:630px;font-size:19px}
.welcome-title span{color:var(--blue);font-family:"PT Serif",serif;text-transform:none}
.welcome-text{left:243px;top:716px;width:340px;font-size:10.5px}
.welcome-photo{left:303px;top:813px;width:288px;height:169px;background:linear-gradient(135deg,#c9c2bb,#7d7268 55%,#3d3733)}
.more{left:243px;top:900px;width:66px;height:66px;border-radius:50%;background:var(--blue);color:var(--white);font-family:"Oswald",sans-serif;font-size:11px;display:flex;align-items:center;justify-content:center}
.vline{left:674px;top:598px;width:0;height:362px;border-left:2px dotted var(--blue)}
.feat-ph{width:70px;height:70px;border-radius:50%;background:radial-gradient(circle at 40% 40%,#f0d2b4,#b58a5c 60%,#6e5237)}
.feat-title{left:729px;font-size:12.5px}
.feat-text{left:729px;width:230px;font-size:10px;line-height:1.4}
.band-blue{left:0;top:1040px;width:1200px;height:368px;background:var(--blue)}
.band-light{left:0;top:1408px;width:1200px;height:276px;background:var(--light)}
.p-title{color:var(--white)}
.p-sub{color:#e5f0f6}
.p-rule{left:520px;top:1160px;width:160px;height:1px;background:rgba(255,255,255,.6)}
.cat-title{left:243px;top:1226px;color:var(--white);font-size:14px;font-family:"Oswald",sans-serif;font-weight:400}
.cat-text{left:243px;top:1255px;width:170px;color:#eaf3f8;font-size:10px}
.pill{top:1314px;height:24px;border:1px solid var(--white);border-radius:12px;background:var(--white);color:var(--blue);font-family:"Oswald",sans-serif;font-size:9px;display:flex;align-items:center;justify-content:center}
.pill.outline{background:transparent;color:var(--white)}
.bag-hero{left:510px;top:1202px;width:203px;height:259px;border-radius:6px;background:linear-gradient(180deg,#e9c88a,#d9a55a 50%,#c9763a)}
.feat-list{left:792px;top:1226px;color:var(--white)}
.feat-list h4{font-family:"Oswald",sans-serif;font-weight:400;font-size:14px;margin-bottom:10px}
.feat-list li{list-style:none;font-size:10px;color:#eef5f9;height:20px;display:flex;align-items:center;gap:7px}
.feat-list li i{width:8px;height:8px;border-radius:50%;background:var(--white);display:inline-block}
.mini{width:72px;height:90px;border-radius:5px}
.mini-label{font-family:"Oswald",sans-serif;font-size:9px;color:var(--ink);text-align:center;width:90px}
.n-title{top:1738px}
.n-sub{top:1780px}
.ring{left:459px;top:1857px;width:282px;height:282px;border-radius:50%;border:2px solid #eef2f5}
.n-icon{width:56px;height:56px;border-radius:50%;background:var(--blue);display:flex;align-items:center;justify-content:center}
.n-head{font-size:12.5px}
.n-txt{font-size:10px;line-height:1.35;width:200px}
.right{text-align:right}
.n-products{left:523px;top:1900px;width:155px;height:115px;border-radius:6px;background:linear-gradient(135deg,#d9e6ee,#b9cfdc 40%,#e6b49a 70%,#c9d9e4)}
.contact-lbl{left:0;width:1200px;text-align:center;top:2040px;font-family:"Oswald",sans-serif;color:var(--blue);font-size:9px}
.contact-phone{left:0;width:1200px;text-align:center;top:2055px;font-family:"Oswald",sans-serif;color:var(--accent);font-size:16px}
.testi-bg{left:0;top:2182px;width:1200px;height:318px;background:linear-gradient(100deg,#3a332c,#5a4b3b 40%,#4a4438 70%,#2e2c28)}
.avatar{width:64px;height:64px;border-radius:50%;background:radial-gradient(circle,#c9a98a,#6e5a48);border:3px solid rgba(255,255,255,.8)}
.t-name{font-family:"Oswald",sans-serif;font-size:12px;color:var(--white)}
.t-name span{color:var(--blue)}
.t-text{font-size:10px;color:#eee;width:240px;line-height:1.35}
.tdot{width:6px;height:6px;border-radius:50%;background:rgba(255,255,255,.4);top:2449px}
.w-title{top:2558px}
.w-sub{top:2595px}
.w-rule{left:520px;top:2622px;width:160px;height:1px;background:#ddd}
.w-rule i{position:absolute;left:60px;top:-1px;width:40px;height:3px;background:var(--green)}
.w-vline{left:533px;top:2690px;height:310px;border-left:2px dotted var(--blue)}
.w-head{font-size:12.5px;width:300px;text-align:right;left:193px}
.w-txt{font-size:10px;width:300px;text-align:right;left:193px;line-height:1.35}
.w-art{left:607px;top:2720px;width:352px;height:325px;border-radius:8px;background:linear-gradient(120deg,#6b4530 0%,#8a5c3d 35%,#e7ddd2 55%,#d95a45 80%,#f2efe9)}
.cloud{left:792px;top:2658px;width:132px;height:88px;border-radius:44px;background:var(--blue);color:var(--white);text-align:center;padding-top:16px;font-family:"Oswald",sans-serif}
.cloud small{display:block;font-family:"PT Serif",serif;font-size:9px}
.cloud b{display:block;font-weight:400;font-size:15px;line-height:1.1}
.deal{left:0;top:3100px;width:600px;height:323px;background:var(--blue)}
.coupon{left:600px;top:3100px;width:600px;height:323px;background:var(--dark)}
.deal-bag{left:53px;top:3115px;width:176px;height:300px;border-radius:6px;background:linear-gradient(180deg,#bcd0dd 0%,#e2e7ea 45%,#b24a32 75%,#6d2417)}
.deal-title{left:243px;top:3156px;color:var(--white);font-family:"Oswald",sans-serif;font-weight:400;font-size:20px}
.deal-sub{left:243px;top:3187px;color:var(--white);font-size:9px}
.deal-sub b{color:var(--accent);font-family:"Oswald",sans-serif;font-weight:400;font-size:13px}
.count-strip{left:241px;top:3213px;width:359px;height:52px;background:#b3d1e3}
.count{top:3218px;width:64px;text-align:center}
.count b{display:block;font-family:"Oswald",sans-serif;font-weight:400;font-size:18px;color:var(--blue-dark)}
.count span{font-size:8px;letter-spacing:.5px;color:var(--white)}
.deal-list{left:330px;top:3278px;color:var(--white);font-size:10px}
.deal-list li{list-style:none;height:20px;display:flex;align-items:center;gap:7px}
.deal-list li i{width:5px;height:5px;border-radius:50%;background:var(--white)}
.shop{left:222px;top:3288px;width:60px;height:60px;border-radius:50%;background:var(--white);color:var(--ink);font-family:"Oswald",sans-serif;font-size:10px;line-height:1.1;display:flex;align-items:center;justify-content:center;text-align:center}
.c-title{left:660px;top:3154px;color:var(--white);font-family:"Oswald",sans-serif;font-weight:400;font-size:20px}
.c-sub{left:660px;top:3183px;color:var(--white);font-family:"Roboto",sans-serif;font-size:9px}
.field{height:27px;border:1px solid #ddd;background:var(--white);color:#aaa;font-size:9px;padding:7px 8px}
.c-lbl{color:var(--white);font-size:10px}
.submit{left:660px;top:3343px;width:98px;height:26px;border-radius:13px;background:var(--blue);color:var(--white);font-family:"Oswald",sans-serif;font-size:10px;display:flex;align-items:center;justify-content:center}
.arrow{width:22px;height:22px;border-radius:50%;border:1px solid #ccc;top:3491px;display:flex;align-items:center;justify-content:center}
.partner{width:100px;height:36px;border-radius:18px;background:#e9eeea;top:3484px}
.b-title{top:3632px}
.b-sub{top:3676px}
.card-img{top:3731px;width:220px;height:150px;background:linear-gradient(135deg,#e5ddd5,#8f7b6a 55%,#3f3630)}
.badge{top:3861px;width:40px;height:40px;border-radius:50%;background:var(--blue);color:var(--white);font-family:"Oswald",sans-serif;font-size:9px;line-height:1.1;display:flex;align-items:center;justify-content:center;text-align:center}
.card-title{top:3911px;width:220px;font-size:12px;line-height:1.3}
.card-text{top:3956px;width:215px;font-family:"Roboto",sans-serif;font-size:10px;color:#888;line-height:1.3}
.read{top:4025px;width:84px;height:24px;border-radius:12px;border:1px solid #bbb;font-family:"Oswald",sans-serif;font-size:10px;color:var(--ink);display:flex;align-items:center;justify-content:center}
.footer{left:0;top:4110px;width:1200px;height:255px;background:linear-gradient(90deg,#161515,#2a211e 60%,#3a1a16)}
.f-head{color:var(--white);font-family:"Oswald",sans-serif;font-weight:400;font-size:11px;top:4164px}
.f-list{top:4199px;color:#ccc;font-size:9.5px}
.f-list li{list-style:none;height:21px;display:flex;align-items:center;gap:8px}
.f-list li i{width:9px;height:9px;border-radius:2px;background:#ccc;display:inline-block}
.f-list li b{width:4px;height:4px;border-radius:50%;background:#ccc;display:inline-block}
.f-coupon{left:792px;top:4166px;width:164px;height:143px;border:1px dashed #888;color:var(--white);text-align:center;padding-top:34px}
.f-coupon .big{font-family:"Oswald",sans-serif;font-size:13px}
.f-coupon .big b{color:var(--blue);font-size:28px;font-weight:400}
.f-coupon .s1{font-family:"Oswald",sans-serif;font-size:9px;margin-top:2px}
.f-coupon .s2{font-size:9px;margin-top:10px;color:#ddd}
.subscribe{left:0;top:4365px;width:1200px;height:105px;background:var(--blue)}
.s-title{left:243px;top:4400px;color:var(--white);font-family:"Oswald",sans-serif;font-weight:400;font-size:16px}
.s-sub{left:243px;top:4423px;color:#eaf3f8;font-size:9px}
.s-input{left:463px;top:4405px;width:248px;height:27px;border:1px solid var(--white);border-radius:14px;color:#e2eef5;font-size:9px;padding:7px 12px}
.social{top:4407px;width:26px;height:26px;border-radius:50%;border:1px solid var(--white)}
.bottom{left:0;top:4470px;width:1200px;height:62px;background:#1d1a19}
.copy{left:243px;top:4494px;color:#999;font-size:9px}
.copy b{color:var(--blue);font-weight:400}
.b-links{top:4494px;font-family:"Roboto",sans-serif;font-size:8px;color:#999}
</style>
</head>
<body>

<div class="abs hero-photo" role="img" aria-label="Foto: Frau spielt mit ihren Hunden auf einer sonnigen Wiese"></div>
<div class="abs hero-shade"></div>
<svg class="abs" style="left:0;top:520px" width="1200" height="62" viewBox="0 0 1200 62"><path d="M0 58 Q600 -10 1200 38 L1200 62 L0 62Z" fill="#fff"/></svg>
<nav class="nav">
  <a class="active" style="left:243px">START</a>
  <a style="left:304px">ÜBER UNS</a>
  <a style="left:385px">FÜR HUNDE</a>
  <a style="left:466px">FÜR KATZEN</a>
  <a style="left:688px">ERNÄHRUNG</a>
  <a style="left:774px">BLOG</a>
  <a style="left:832px">SHOP</a>
  <a style="left:898px">KONTAKT</a>
</nav>
<div class="abs logo">VELORA</div>

<div class="abs hero-name">CHESTER</div>
<div class="abs hero-line1">IST EIN CHAMPION.</div>
<div class="abs hero-line2">FÜTTERE IHN AUCH WIE EINEN.</div>
<div class="abs hero-rule"></div>
<p class="abs hero-text">Bei Velora stellen wir Hund und Katze auf natürliche, artgerechte Fütterung um – ohne Zucker und Zusatzstoffe.</p>
<div class="abs hero-link"><span class="dot"></span>ZU UNSEREN ERNÄHRUNGSPLÄNEN</div>

<h2 class="abs head welcome-title">Willkommen bei <span>"Velora"</span></h2>
<p class="abs welcome-text">Natürliche Ernährung für Hund und Katze: teils roh, teils gekocht, angepasst an Grösse, Rasse und Alter – auch speziell für Welpen.</p>
<div class="abs welcome-photo" role="img" aria-label="Foto: kleiner Hund liegt neben seiner Halterin auf dem Bett"></div>
<div class="abs more">MEHR</div>
<div class="abs vline"></div>

<div class="abs feat-ph" style="left:639px;top:655px" role="img" aria-label="Foto: Kind mit Hund"></div>
<h3 class="abs head feat-title" style="top:662px">Artgerechte Fütterung</h3>
<p class="abs feat-text" style="top:682px">Ohne Geschmacksverstärker, Zucker und Zusatzstoffe, die Ihrem Tier gesundheitlich schaden können.</p>
<div class="abs feat-ph" style="left:639px;top:766px" role="img" aria-label="Foto: Kind umarmt einen Welpen"></div>
<h3 class="abs head feat-title" style="top:773px">Persönliche Beratung</h3>
<p class="abs feat-text" style="top:793px">Bei Übergewicht, Allergien, Unverträglich­keiten und Magen-Darm-Problemen.</p>
<div class="abs feat-ph" style="left:639px;top:878px" role="img" aria-label="Foto: lachendes Kind mit Haustier"></div>
<h3 class="abs head feat-title" style="top:885px">Speziell für Welpen</h3>
<p class="abs feat-text" style="top:905px">Ein sanfter Start mit Futterplänen, die mit Ihrem Welpen Schritt für Schritt mitwachsen.</p>

<div class="abs band-blue"></div>
<div class="abs band-light"></div>
<svg class="abs" style="left:0;top:1408px" width="1200" height="276" viewBox="0 0 1200 276">
  <path d="M60 40 Q600 300 1140 40" fill="none" stroke="#e6e6e6"/>
  <path d="M0 20 Q600 340 1200 20" fill="none" stroke="#ececec"/>
</svg>
<h2 class="abs title p-title" style="top:1092px">Unsere Produkte</h2>
<p class="abs sub p-sub" style="top:1133px">Hausgemacht und auf Vorbestellung: Kekse, Leckerlies, Snacks und Hausmannskost im Glas.</p>
<div class="abs p-rule"></div>
<h3 class="abs cat-title">HAUSMANNSKOST</h3>
<p class="abs cat-text">Schonend gekocht und im Einmachglas abgefüllt – alles auf Vorbestellung [...]</p>
<div class="abs pill" style="left:243px;width:78px">FÜR HUNDE</div>
<div class="abs pill outline" style="left:327px;width:78px">FÜR KATZEN</div>
<div class="abs bag-hero" role="img" aria-label="Produktfoto: Beutel mit hausgemachten Hähnchen-Streifen und Karotten"></div>
<div class="abs feat-list">
  <h4>BERATUNG BEI</h4>
  <ul>
    <li><i></i>Übergewicht</li>
    <li><i></i>Allergien</li>
    <li><i></i>Unverträglichkeiten</li>
    <li><i></i>Magen-Darm-Problemen</li>
    <li><i></i>Individuelle Ernährungspläne</li>
  </ul>
</div>

<div class="abs mini" style="left:267px;top:1460px;background:linear-gradient(180deg,#eee,#c64a3a)" role="img" aria-label="Beutel mit Keksen"></div>
<div class="abs mini-label" style="left:258px;top:1552px">KEKSE</div>
<div class="abs mini" style="left:381px;top:1488px;background:linear-gradient(180deg,#f3e9d9,#d48a4a)" role="img" aria-label="Beutel mit Leckerlies"></div>
<div class="abs mini-label" style="left:372px;top:1580px">LECKERLIES</div>
<div class="abs mini" style="left:497px;top:1507px;background:linear-gradient(180deg,#e9c88a,#c9763a)" role="img" aria-label="Glas mit Hausmannskost"></div>
<div class="abs mini-label" style="left:488px;top:1599px;color:var(--blue)">HAUSMANNSKOST</div>
<div class="abs mini" style="left:610px;top:1507px;background:linear-gradient(180deg,#e2e6ee,#5a6fa8)" role="img" aria-label="Schachtel mit Pralinen"></div>
<div class="abs mini-label" style="left:602px;top:1599px">PRALINEN</div>
<div class="abs mini" style="left:742px;top:1488px;background:linear-gradient(180deg,#dfeaf3,#8fb0d1)" role="img" aria-label="Beutel mit Snacks"></div>
<div class="abs mini-label" style="left:733px;top:1580px">SNACKS</div>
<div class="abs mini" style="left:859px;top:1460px;background:linear-gradient(180deg,#d6dbe0,#8b9198)" role="img" aria-label="Einmachglas mit Futter"></div>
<div class="abs mini-label" style="left:851px;top:1552px">EINMACHGLÄSER</div>

<h2 class="abs title n-title">Unsere Ernährungsphilosophie</h2>
<p class="abs sub n-sub">Jede Fütterung beginnt bei uns mit frischen, natürlichen Zutaten – ganz ohne Zusatzstoffe.</p>
<div class="abs ring"></div>
<div class="abs n-products" role="img" aria-label="Gruppe von Futterbeuteln und Gläsern"></div>
<div class="abs contact-lbl">RUFEN SIE UNS AN</div>
<div class="abs contact-phone">(04) 21-555-0188</div>

<h3 class="abs head n-head right" style="left:252px;width:200px;top:1866px">Ohne Zucker</h3>
<p class="abs n-txt" style="left:246px;top:1886px">Keine unnötigen Geschmacks­verstärker oder Zucker.</p>
<h3 class="abs head n-head right" style="left:218px;width:200px;top:1970px">Teils roh</h3>
<p class="abs n-txt right" style="left:268px;top:1990px;width:150px">Frisches Fleisch und Gemüse als artgerechte Basis.</p>
<h3 class="abs head n-head right" style="left:252px;width:200px;top:2074px">Teils gekocht</h3>
<p class="abs n-txt right" style="left:236px;top:2094px;width:200px">Schonend gegart und leicht verdaulich für empfindliche Mägen.</p>

<h3 class="abs head n-head" style="left:746px;top:1866px">Nach Grösse</h3>
<p class="abs n-txt" style="left:746px;top:1886px">Portionen, die genau zum Energiebedarf Ihres Tieres passen.</p>
<h3 class="abs head n-head" style="left:781px;top:1970px">Nach Rasse</h3>
<p class="abs n-txt" style="left:781px;top:1990px">Jede Rasse hat eigene Bedürfnisse – wir berücksichtigen sie.</p>
<h3 class="abs head n-head" style="left:746px;top:2074px">Nach Alter</h3>
<p class="abs n-txt" style="left:746px;top:2094px">Vom Welpen bis zum Senior mit angepasster Ernährung.</p>

<div class="abs n-icon" style="left:463px;top:1864px"><svg width="22" height="22" viewBox="0 0 22 22"><path d="M5 17 L17 5" stroke="#fff" stroke-width="3" stroke-linecap="round"/></svg></div>
<div class="abs n-icon" style="left:430px;top:1970px"><svg width="22" height="22" viewBox="0 0 22 22"><path d="M11 4v14M4 11h14" stroke="#fff" stroke-width="4" stroke-linecap="round"/></svg></div>
<div class="abs n-icon" style="left:463px;top:2072px"><svg width="22" height="22" viewBox="0 0 22 22"><ellipse cx="10" cy="11" rx="7" ry="4.5" fill="#fff"/><path d="M16 11 L21 7 L21 15Z" fill="#fff"/></svg></div>
<div class="abs n-icon" style="left:680px;top:1864px"><svg width="22" height="22" viewBox="0 0 22 22"><path d="M4 16 A7 7 0 1 1 18 16" fill="none" stroke="#fff" stroke-width="3"/></svg></div>
<div class="abs n-icon" style="left:713px;top:1970px"><svg width="22" height="22" viewBox="0 0 22 22"><path d="M8 4 Q16 7 8 11 Q0 15 14 18" fill="none" stroke="#fff" stroke-width="2.5"/></svg></div>
<div class="abs n-icon" style="left:680px;top:2072px"><svg width="22" height="22" viewBox="0 0 22 22"><path d="M5 17 L17 5" stroke="#fff" stroke-width="3" stroke-linecap="round"/><circle cx="16" cy="6" r="3" fill="#fff"/></svg></div>

<div class="abs testi-bg" role="img" aria-label="Dunkles Foto: Hund läuft neben seinem Halter auf einer Strasse"></div>
<svg class="abs" style="left:0;top:2180px" width="1200" height="30" viewBox="0 0 1200 30"><path d="M0 0 L1200 0 L1200 8 Q600 40 0 4Z" fill="#fff"/></svg>
<div class="abs avatar" style="left:243px;top:2326px" role="img" aria-label="Porträt einer Kundin"></div>
<div class="abs t-name" style="left:320px;top:2315px">LENA BRANDT / <span>HUNDEHALTERIN</span></div>
<p class="abs t-text" style="left:320px;top:2334px">Sein Fell glänzt wieder und die Allergie ist weg! Danke für die tolle Beratung und die natürlichen Rezepte!</p>
<div class="abs avatar" style="left:609px;top:2326px" role="img" aria-label="Porträt eines Kunden"></div>
<div class="abs t-name" style="left:686px;top:2315px">MIRKO HALS / <span>KATZENHALTER</span></div>
<p class="abs t-text" style="left:686px;top:2334px">Endlich keine Magenprobleme mehr! Der Ernährungsplan war genau auf unsere Katze abgestimmt. Herzlichen Dank!</p>
<div class="abs tdot" style="left:580px;background:var(--blue)"></div>
<div class="abs tdot" style="left:597px"></div>
<div class="abs tdot" style="left:614px"></div>

<h2 class="abs title w-title">Unsere Accessoires</h2>
<p class="abs sub w-sub">Natürliche Materialien und durchdachtes Zubehör für Tiere sowie für Frauchen und Herrchen.</p>
<div class="abs w-rule"><i></i></div>
<div class="abs w-vline"></div>

<h3 class="abs head w-head" style="top:2686px">Halsbänder &amp; Leinen</h3>
<p class="abs w-txt" style="top:2706px">Aus natürlichen Materialien wie Leder, Hanf und Baumwolle gefertigt.</p>
<h3 class="abs head w-head" style="top:2779px">Geschirre</h3>
<p class="abs w-txt" style="top:2799px">Bequem, atmungsaktiv und passend für jede Grösse und Rasse.</p>
<h3 class="abs head w-head" style="top:2874px">Lern- &amp; Spielzeug</h3>
<p class="abs w-txt" style="top:2894px">Aus Holz und Stoff, robust und frei von Schadstoffen.</p>
<h3 class="abs head w-head" style="top:2967px">Für Frauchen &amp; Herrchen</h3>
<p class="abs w-txt" style="top:2987px">Diverses Zubehör rund ums Füttern, Spazieren und Pflegen.</p>

<div class="abs n-icon" style="left:505px;top:2682px"><svg width="22" height="22" viewBox="0 0 22 22"><circle cx="8" cy="7" r="3" fill="#fff"/><circle cx="14" cy="7" r="3" fill="#fff"/><circle cx="11" cy="13" r="3" fill="#fff"/><circle cx="11" cy="18" r="2" fill="#fff"/></svg></div>
<div class="abs n-icon" style="left:505px;top:2776px"><svg width="22" height="22" viewBox="0 0 22 22"><path d="M11 3v16M4 6h14M6 18h10" stroke="#fff" stroke-width="2"/><path d="M2 12 L4 6 L6 12Z M16 12 L18 6 L20 12Z" fill="#fff"/></svg></div>
<div class="abs n-icon" style="left:505px;top:2871px"><svg width="22" height="22" viewBox="0 0 22 22"><path d="M3 14 Q11 2 19 14Z" fill="#fff"/><rect x="3" y="15" width="16" height="3" fill="#fff"/></svg></div>
<div class="abs n-icon" style="left:505px;top:2964px"><svg width="22" height="22" viewBox="0 0 22 22"><path d="M4 18 Q11 2 18 18Z" fill="none" stroke="#fff" stroke-width="2"/><path d="M3 18h16" stroke="#fff" stroke-width="2"/></svg></div>

<div class="abs w-art" role="img" aria-label="Foto: brauner Labrador neben Futterbeuteln und Gläsern"></div>
<div class="abs cloud"><small>Inklusive einer</small><b>ÜBERRASCHUNG<br>IM PAKET!</b></div>
<div class="abs" style="left:810px;top:2752px;width:16px;height:16px;border-radius:50%;background:var(--blue)"></div>
<div class="abs" style="left:798px;top:2774px;width:9px;height:9px;border-radius:50%;background:var(--blue)"></div>

<div class="abs deal"></div>
<div class="abs coupon"></div>
<div class="abs count-strip"></div>
<div class="abs deal-bag" role="img" aria-label="Futterbeutel mit einem rohen Lammkarree"></div>
<div class="abs shop">ZUM<br>SHOP</div>
<h3 class="abs deal-title">ANGEBOT DER WOCHE</h3>
<p class="abs deal-sub">Bis zu <b>40% auf Leckerlies</b></p>
<div class="abs count" style="left:242px"><b>00</b><span>TAGE</span></div>
<div class="abs count" style="left:309px"><b>00</b><span>STUNDEN</span></div>
<div class="abs count" style="left:387px"><b>00</b><span>MINUTEN</span></div>
<div class="abs count" style="left:470px"><b>00</b><span>SEKUNDEN</span></div>
<ul class="abs deal-list">
  <li><i></i>Ohne Zucker und Zusatzstoffe</li>
  <li><i></i>Selbst gebacken und von Hand verpackt</li>
  <li><i></i>Glutenfrei</li>
  <li><i></i>Nur auf Vorbestellung erhältlich</li>
</ul>

<h3 class="abs c-title">GUTSCHEIN HOLEN</h3>
<p class="abs c-sub">FORMULAR AUSFÜLLEN UND GRATIS PROBEPAKET ERHALTEN</p>
<div class="abs field" style="left:660px;top:3209px;width:167px">Ihr Name *</div>
<div class="abs field" style="left:848px;top:3209px;width:167px">Ihre E-Mail *</div>
<div class="abs field" style="left:660px;top:3252px;width:167px">Telefon *</div>
<div class="abs field" style="left:848px;top:3252px;width:167px;display:flex;justify-content:space-between">Ihr Land *<svg width="8" height="8" viewBox="0 0 8 8"><path d="M1 3l3 3 3-3" stroke="#aaa" fill="none"/></svg></div>
<div class="abs c-lbl" style="left:660px;top:3304px">Ich habe Hund(e)</div>
<div class="abs field" style="left:752px;top:3298px;width:75px"></div>
<div class="abs c-lbl" style="left:848px;top:3304px">&amp; Katze(n)</div>
<div class="abs field" style="left:910px;top:3298px;width:105px"></div>
<div class="abs submit">ABSENDEN</div>

<div class="abs arrow" style="left:232px"><svg width="8" height="8" viewBox="0 0 8 8"><path d="M5 1L2 4l3 3" stroke="#aaa" fill="none"/></svg></div>
<div class="abs arrow" style="left:946px"><svg width="8" height="8" viewBox="0 0 8 8"><path d="M3 1l3 3-3 3" stroke="#aaa" fill="none"/></svg></div>
<div class="abs partner" style="left:263px;background:#dfe9dc"></div>
<div class="abs partner" style="left:406px"></div>
<div class="abs partner" style="left:550px"></div>
<div class="abs partner" style="left:691px"></div>
<div class="abs partner" style="left:834px"></div>

<h2 class="abs title b-title">Aktuelle Blogbeiträge</h2>
<p class="abs sub b-sub">Tipps zu natürlicher Ernährung, hausgemachten Snacks und gesunden Gewohnheiten.</p>

<div class="abs card-img" style="left:246px" role="img" aria-label="Foto: Frau mit ihrem Hund zu Hause"></div>
<div class="abs badge" style="left:258px">MÄR<br>25</div>
<h3 class="abs head card-title" style="left:246px">Gesunde Joghurt-Snacks zum Selbermachen!</h3>
<p class="abs card-text" style="left:246px">Gefrorener Joghurt mit Obst ist an warmen Tagen eine leckere und gesunde Belohnung, die Sie ganz leicht selbst zubereiten.</p>
<div class="abs read" style="left:246px">WEITERLESEN</div>

<div class="abs card-img" style="left:489px" role="img" aria-label="Foto: kleiner Hund auf einem Bett"></div>
<div class="abs badge" style="left:501px">MÄR<br>25</div>
<h3 class="abs head card-title" style="left:489px">Rohfütterung: So gelingt der Einstieg</h3>
<p class="abs card-text" style="left:489px">Die Umstellung auf teils rohe, teils gekochte Kost braucht Zeit. Wir zeigen, wie Ihr Tier sich Schritt für Schritt daran gewöhnt.</p>
<div class="abs read" style="left:489px">WEITERLESEN</div>

<div class="abs card-img" style="left:734px" role="img" aria-label="Foto: Mops wird im Arm gehalten"></div>
<div class="abs badge" style="left:746px">MÄR<br>25</div>
<h3 class="abs head card-title" style="left:734px">Hausgemachte Kekse: 3 kaufen, 1 gratis!</h3>
<p class="abs card-text" style="left:734px">Diesen Monat gibt es zu drei Gläsern unserer Kekse ein viertes gratis dazu. Einfach vorbestellen und abholen.</p>
<div class="abs read" style="left:734px">WEITERLESEN</div>

<div class="abs footer"></div>
<h4 class="abs f-head" style="left:243px">KONTAKT</h4>
<ul class="abs f-list" style="left:243px">
  <li><i></i>hello@velora-pet.com</li>
  <li><i></i>01-222-555-0142</li>
  <li><i></i>www.velora-pet.com</li>
  <li><i></i>4410 Lindenweg, Basel 12</li>
</ul>
<h4 class="abs f-head" style="left:445px">UNTERNEHMEN</h4>
<ul class="abs f-list" style="left:445px">
  <li><b></b>Über uns</li><li><b></b>Engagement</li><li><b></b>Presse</li><li><b></b>FAQ</li><li><b></b>Kontakt</li><li><b></b>Händler werden</li>
</ul>
<h4 class="abs f-head" style="left:609px">WEITERE LINKS</h4>
<ul class="abs f-list" style="left:609px">
  <li><b></b>Beratung</li><li><b></b>Ernährungspläne</li><li><b></b>Termin vereinbaren</li><li><b></b>Accessoires</li><li><b></b>Preise &amp; Versand</li>
</ul>
<div class="abs f-coupon">
  <div class="big">SPARE <b>10%</b></div>
  <div class="s1">AUF DIE ERSTBERATUNG</div>
  <div class="s2">Gutscheincode: treat10</div>
</div>

<div class="abs subscribe"></div>
<h3 class="abs s-title">NEWSLETTER ABONNIEREN!</h3>
<p class="abs s-sub">Monatliche Tipps zur Ernährung</p>
<div class="abs s-input">Ihre E-Mail-Adresse</div>
<div class="abs social" style="left:804px"></div>
<div class="abs social" style="left:836px"></div>
<div class="abs social" style="left:868px"></div>
<div class="abs social" style="left:900px"></div>
<div class="abs social" style="left:932px"></div>

<div class="abs bottom"></div>
<p class="abs copy">© Copyright <b>Velora</b> 2016. Alle Rechte vorbehalten.</p>
<div class="abs b-links" style="left:609px">START</div>
<div class="abs b-links" style="left:655px">ÜBER UNS</div>
<div class="abs b-links" style="left:714px">ANGEBOT</div>
<div class="abs b-links" style="left:772px">BLOG</div>
<div class="abs b-links" style="left:815px">KONTAKT</div>

</body>
</html>
```